Forget what you know about corporate well

I need a one-page flies used for print, to embedding in a website, all social media platforms and email.

Target Market(s)

Business

Industry/Entity Type

Health And Wellness

Font styles to use
Serif
Script
Other font styles liked:
• I would like the designers opinion on the font

Colors

Designer to choose colors to be used in the design.

Requirements
Must have
• This is the wording:
• Did you know that 75% of healthcare costs are incurred by preventable diseases? Cardiovascular disease, cancer, and diabetes are the three major causes of rising health care plans and are all preventable.
• Owen and his team have spent decades learning how to increase productivity, reduce absenteeism, and increase employee engagement, all leading to lowering healthcare costs. Together, they have developed a system created to target the masses all while addressing individual needs. Their corporate training challenges helps to engrain positive habits through a carefully curated accountability and reward system.
• How it works:
• Step 1 – evaluate the needs of your business;
• Step 2 – set up individualized workshops based on highest needs;
• Step 3 – create a customized corporate training challenge.
• Why Owen?
• Owen excels at motivational speaking. He is an author, a nutritionist and a professional athlete with a master’s degree in clinical nutrition. He is a teacher of corporate wellness at Marbrook College and a health coach. Owen has been featured in national magazines, podcasts, and popular fitness websites. Owen’s own health issues put him on a quest to heal himself and others. With twenty-five years of experience and a passion for wellness, he can provide your company with an unforgettable experience.
Nice to have
• I will not give my opinion, I believe that is an insult to the designer. All of the verbiage is above and I attached a plethora of pictures.
Should not have
• No opinion

```html
<!DOCTYPE html>
<html lang="en">
<head>
<meta charset="utf-8">
<title>Corporate Wellness Flyer – Owen</title>
<link rel="stylesheet" href="https://fonts.googleapis.com/css2?family=Barlow:wght@300;400;600;700&family=Barlow+Semi+Condensed:ital,wght@0,300;0,400;0,600;1,700&display=swap">
<style>
  :root{
    --lime:#b8c230;
    --lime-band:#cbd948;
    --maroon:#8a1c3c;
    --slate:#676767;
    --mist:#c6c6c6;
    --white:#ffffff;
  }
  html,body{margin:0;padding:0;overflow:hidden;background:#fff;}
  .flyer{
    position:relative;width:845px;height:1200px;overflow:hidden;
    background:var(--white);font-family:"Barlow",sans-serif;
  }
  .backdrop{position:absolute;inset:0;width:845px;height:1200px;}
  .headline{
    position:absolute;left:68px;top:56px;width:730px;margin:0;
    font-family:"Barlow Semi Condensed",sans-serif;font-weight:300;
    font-size:65px;line-height:68px;color:var(--lime);letter-spacing:-0.3px;
  }
  .lead{
    position:absolute;left:69px;top:291px;margin:0;white-space:nowrap;
    font-family:"Barlow Semi Condensed",sans-serif;font-weight:600;
    font-size:22px;line-height:29px;color:var(--maroon);
  }
  .intro{
    position:absolute;left:69px;top:492px;margin:0;white-space:nowrap;
    font-family:"Barlow",sans-serif;font-weight:600;
    font-size:15.5px;line-height:24.2px;color:var(--white);letter-spacing:-0.45px;
  }
  .steps{
    position:absolute;left:0;top:848px;width:845px;height:100px;
    margin:0;padding:0;list-style:none;
  }
  .step{
    position:absolute;top:0;width:220px;text-align:center;
    font-family:"Barlow",sans-serif;font-weight:300;
    font-size:18.5px;line-height:24px;color:var(--white);letter-spacing:0.3px;
  }
  .step--one{left:20px;}
  .step--two{left:289px;}
  .step--three{left:576px;}
  .step__label{
    display:block;font-family:"Barlow Semi Condensed",sans-serif;
    font-weight:700;font-style:italic;font-size:18px;
    color:var(--lime-band);letter-spacing:0;
  }
  .why{
    position:absolute;left:70px;top:978px;
  }
  .why__title{
    margin:0 0 6px;font-family:"Barlow",sans-serif;font-weight:700;
    font-size:19px;color:var(--mist);letter-spacing:0.3px;
  }
  .why__text{
    margin:0;white-space:nowrap;
    font-family:"Barlow Semi Condensed",sans-serif;font-weight:400;
    font-size:14px;line-height:19.3px;color:var(--white);
  }
  .brand{
    position:absolute;left:556px;top:1010px;width:250px;
    display:flex;flex-direction:column;align-items:center;gap:16px;
  }
  .brand__mark{width:44px;height:44px;border-radius:50%;background:var(--lime-band);}
  .brand__name{
    font-family:"Barlow",sans-serif;font-weight:700;font-size:21px;
    color:var(--lime-band);letter-spacing:0.2px;white-space:nowrap;
  }
</style>
</head>
<body>
<main class="flyer">
  <svg class="backdrop" viewBox="0 0 845 1200">
    <defs>
      <linearGradient id="portrait-tone" x1="0" y1="0" x2="0" y2="1">
        <stop offset="0" stop-color="#d9b49c"/>
        <stop offset="0.55" stop-color="#c79a80"/>
        <stop offset="1" stop-color="#8a2a35"/>
      </linearGradient>
    </defs>
    <path class="band-lime" d="M0 428 C 220 420 520 438 845 502 L845 800 L0 820 Z" fill="var(--lime-band)"/>
    <rect role="img" aria-label="Portrait photo of Owen smiling, wearing a dark red polo shirt"
          x="500" y="280" width="345" height="520" fill="url(#portrait-tone)"/>
    <path class="band-divider" d="M0 810 C 240 782 500 774 845 784 L845 1200 L0 1200 Z" fill="var(--white)"/>
    <path class="band-slate" d="M0 820 C 240 792 500 784 845 794 L845 1200 L0 1200 Z" fill="var(--slate)"/>
    <g class="step-dividers" fill="none" stroke="var(--lime-band)" stroke-width="2">
      <path d="M253 850 V 888 L 260 896 L 253 904 V 942"/>
      <path d="M545 850 V 888 L 552 896 L 545 904 V 942"/>
    </g>
  </svg>

  <h1 class="headline">Did you know that 75% of healthcare costs are incurred by preventable diseases?</h1>

  <p class="lead">Cardiovascular disease, cancer, and diabetes<br>are the three major causes of rising health<br>care plans and are all preventable.</p>

  <p class="intro">Owen and his team have spent decades learning how<br>to increase productivity, reduce absenteeism, and<br>increase employee engagement, all leading to<br>lowering healthcare costs. Together, they have<br>developed a system created to target the masses<br>all while addressing individual needs. Their<br>corporate training challenges helps to<br>engrain positive habits through a<br>carefully curated accountability<br>and reward system.</p>

  <ol class="steps">
    <li class="step step--one"><span class="step__label">STEP 1</span>evaluate the<br>needs of your<br>business</li>
    <li class="step step--two"><span class="step__label">STEP 2</span>set up individualized<br>workshops based on<br>highest needs</li>
    <li class="step step--three"><span class="step__label">STEP 3</span>create a customized<br>corporate training<br>challenge.</li>
  </ol>

  <section class="why">
    <h2 class="why__title">WHY OWEN?</h2>
    <p class="why__text">Owen excels at motivational speaking. He is an author, a nutritionist and a<br>professional athlete with a master’s degree in clinical nutrition. He is a<br>teacher of corporate wellness at Marbrook College and a health coach. Owen<br>has been featured in national magazines, podcasts, and popular fitness<br>websites. Owen’s own health issues put him on a quest to heal himself and<br>others. With twenty-five years of experience and a passion for wellness,<br>he can provide your company with an unforgettable experience.</p>
  </section>

  <div class="brand">
    <span class="brand__mark"></span>
    <span class="brand__name">Elevate Wellness</span>
  </div>
</main>
</body>
</html>
```